promotion company needs a design for there brochure

For a company that does promotional work, work clothing with logo, etc., we have to design a catalog only the outside of the cover. Attached you will find the working drawing and the current cover. Their website and there style; https://www.vandoremerk.be

Font styles to use
Serif

```html
<!DOCTYPE html>
<html lang="nl">
<head>
<meta charset="utf-8">
<title>Vandore Merk – Collectie 2022 cover</title>
<link rel="stylesheet" href="https://fonts.googleapis.com/css2?family=Fira+Sans+Extra+Condensed:wght@300;400;600&display=swap">
<style>
  :root {
    --navy: #233142;
    --navy-deep: #1c2836;
    --teal: #22b897;
    --teal-dark: #1a8f77;
    --mint: #3fdcae;
    --mint-light: #7af5cc;
    --lime: #b3e67c;
    --paper: #eaecf0;
    --stage: #f1f1f0;
    --white: #ffffff;
  }
  html, body {
    margin: 0;
    padding: 0;
    width: 1200px;
    height: 905px;
    overflow: hidden;
    background: var(--stage);
  }
  .cover-spread {
    position: absolute;
    left: 0;
    top: 47px;
    width: 1200px;
    height: 811px;
    display: block;
    font-family: "Fira Sans Extra Condensed", "Arial Narrow", sans-serif;
  }
  .brand-name { fill: var(--white); font-weight: 600; }
  .site-url { fill: var(--mint); font-weight: 400; font-size: 21px; letter-spacing: 0.5px; }
  .service-list { fill: var(--white); font-weight: 300; font-size: 26px; letter-spacing: 1px; }
  .contact { fill: var(--mint); font-weight: 300; font-size: 17px; }
  .contact-heading { fill: var(--white); font-weight: 400; font-size: 17px; }
  .collection-label { fill: var(--mint); font-weight: 300; font-size: 23px; letter-spacing: 1px; }
  .collection-year { fill: var(--mint); font-weight: 300; font-size: 48px; letter-spacing: 1px; }
  .tagline { fill: var(--mint); font-weight: 300; font-size: 33px; letter-spacing: 0.5px; }
</style>
</head>
<body>
<svg class="cover-spread" viewBox="0 0 1376 930" xmlns="http://www.w3.org/2000/svg">
  <defs>
    <linearGradient id="back-photo-tone" x1="0" y1="0" x2="0" y2="1">
      <stop offset="0" stop-color="#3b4a45"/>
      <stop offset="0.5" stop-color="#5a6560"/>
      <stop offset="1" stop-color="#3a4a3f"/>
    </linearGradient>
    <linearGradient id="back-band-fade" x1="0" y1="0" x2="1" y2="0">
      <stop offset="0" stop-color="#1a8f77" stop-opacity="0"/>
      <stop offset="0.55" stop-color="#1a8f77" stop-opacity="0.75"/>
      <stop offset="1" stop-color="#1fa285"/>
    </linearGradient>
    <linearGradient id="cover-photo-tone" x1="0" y1="0" x2="1" y2="0">
      <stop offset="0" stop-color="#4f8f78"/>
      <stop offset="0.45" stop-color="#9fb2ac"/>
      <stop offset="0.75" stop-color="#d9dcdc"/>
      <stop offset="1" stop-color="#5f6a6e"/>
    </linearGradient>
    <linearGradient id="tag-bar" x1="0" y1="0" x2="1" y2="0">
      <stop offset="0" stop-color="var(--teal)"/>
      <stop offset="0.6" stop-color="#3fcf97"/>
      <stop offset="1" stop-color="var(--lime)"/>
    </linearGradient>
    <linearGradient id="mint-streak" x1="0" y1="0" x2="1" y2="0">
      <stop offset="0" stop-color="var(--mint-light)" stop-opacity="0"/>
      <stop offset="1" stop-color="var(--mint-light)"/>
    </linearGradient>
  </defs>

  <!-- back cover -->
  <g class="back-cover">
    <rect class="back-ground" x="0" y="0" width="644" height="930" fill="var(--navy)"/>
    <polygon class="back-photo" role="img" aria-label="Photo of a man in a light jacket seated outdoors among greenery"
             points="364,0 644,0 644,598 364,690" fill="url(#back-photo-tone)" opacity="0.85"/>
    <polygon class="back-band" points="300,712 644,598 644,930 300,930" fill="url(#back-band-fade)"/>

    <text class="brand-name" x="66" y="110" font-size="26">Vandore Merk</text>
    <text class="site-url" x="66" y="153">www.vandoremerk.be</text>

    <line class="rule" x1="66" y1="198" x2="285" y2="198" stroke="var(--teal)" stroke-width="1.5"/>
    <text class="service-list" x="66">
      <tspan x="66" y="232">PROMOTIEKLEDING</tspan>
      <tspan x="66" y="266.5">BORDUREN</tspan>
      <tspan x="66" y="301">SPORTKLEDING</tspan>
      <tspan x="66" y="335.5">RELATIEGESCHENKEN</tspan>
      <tspan x="66" y="370">AUTOBELETTERING</tspan>
      <tspan x="66" y="404.5">WERKKLEDING</tspan>
      <tspan x="66" y="439">BEDRIJFSKLEDING</tspan>
      <tspan x="66" y="473.5">GADGETS</tspan>
      <tspan x="66" y="508">RAAMFOLIES</tspan>
      <tspan x="66" y="542.5">WERKSCHOENEN</tspan>
      <tspan x="66" y="577">T-SHIRT DRUKKEN</tspan>
      <tspan x="66" y="611.5">DIGITALE PRINTING</tspan>
      <tspan x="66" y="646">ZUILEN &amp; BANNERS</tspan>
    </text>
    <line class="rule" x1="66" y1="660" x2="285" y2="660" stroke="var(--teal)" stroke-width="1.5"/>

    <g class="contact-block">
      <text class="contact" x="67" y="733">Beukenstraat 14 BE - 3500 Voorbeek</text>
      <circle cx="78" cy="751" r="8.5" fill="var(--mint)"/>
      <path d="M74.5 746.5 q-1 4 4 8.5 l2-2 2 2 -1.5 1.8 q-6-2-7.8-8.5 z" fill="var(--navy)"/>
      <text class="contact" x="93" y="757">+32(0)11 00 12 34</text>
      <circle cx="234" cy="751" r="8.5" fill="var(--mint)"/>
      <rect x="230.5" y="745" width="7" height="12" rx="1.5" fill="var(--navy)"/>
      <text class="contact" x="249" y="757">+32(0)470 00 56 78</text>
      <text class="contact-heading" x="66" y="787">Openingsuren:</text>
      <text class="contact" x="66" y="810">Ma. - Vrijd. van 10u - 12u &amp; 14u - 18u</text>
      <text class="contact" x="66" y="834">Zaterdag van 10u - 12u</text>
      <text class="contact" x="66" y="858">Zondag en Feestdagen gesloten.</text>
    </g>
  </g>

  <!-- front cover -->
  <g class="front-cover">
    <rect class="front-ground" x="644" y="0" width="732" height="930" fill="var(--paper)"/>
    <polygon class="front-teal-field" points="644,478 1376,236 1376,930 644,930" fill="var(--teal)"/>
    <polygon class="front-photo" role="img" aria-label="Photo collage of a man in sunglasses and a man in a white polo shirt"
             points="768,115 1112,0 1260,0 1260,695 768,695" fill="url(#cover-photo-tone)"/>
    <polygon class="streak" points="688,145 980,38 982,48 690,152" fill="url(#mint-streak)"/>
    <polygon class="streak" points="1000,74 1162,62 1162,66 1000,79" fill="var(--mint-light)" opacity="0.5"/>
    <rect class="photo-edge" x="1258" y="180" width="4" height="515" fill="var(--mint-light)"/>

    <polygon class="collection-badge" points="1190,78 1376,20 1376,140 1190,200" fill="var(--navy)"/>
    <text class="collection-label" x="1219" y="109">COLLECTIE</text>
    <text class="collection-year" x="1218" y="152">2022</text>

    <polygon class="title-panel" points="644,582 1142,418 1142,808 780,930 644,930" fill="var(--navy)"/>
    <polygon class="streak" points="800,930 1095,820 1095,828 826,930" fill="var(--mint-light)" opacity="0.8"/>

    <text class="brand-name" x="798" y="688" font-size="52">Vandore Merk</text>

    <rect class="tag-bar" x="644" y="722" width="132" height="21" fill="url(#tag-bar)"/>
    <rect class="tag-bar" x="644" y="764" width="132" height="21" fill="url(#tag-bar)"/>
    <rect class="tag-bar" x="644" y="805" width="132" height="21" fill="url(#tag-bar)"/>
    <text class="tagline" x="800" y="745">Bedrijfskleding</text>
    <text class="tagline" x="800" y="786">Relatiegeschenken</text>
    <text class="tagline" x="800" y="827">Reclame</text>
  </g>
</svg>
</body>
</html>
```